For our annual dance recital this year we will have an asylum/ orphans/ any spooky shelter. Thats the feel of it.
i will be need an invitation and a ticket.
as the recital will be done in two days the tickets will have same design but different colors.
My idea is to have spooky fonts/ x ray images somehow put in the design.
i will be uploading a lot of images for you to understand where i would like to take this design.
for the invitation i do want to have part of the paper printed in see through material like some of the images uploaded or have an x-ray effect.
the invitation should have this written on it.
MORVANE
Our production is ready and we are dying to have you around. So crawl on over for a spooktacular happening at
IBN TAMRIQ UNIVERSITY AUDITORIUM
The undertaking will begin from 1:30pm to 3:30pm
May 2nd 2014 and May 3rd 2014
The entry tickets will be two colors but same design. i would like it to be printed of see through plastic paper. so we can have one see through and font in black and the other one is dark see through written in white maybe. please make in an xray effext with maybe the pointed feet picture somehow incorporated in the design
i want it to look like the picture i uploaded of (Corbys 4th birthday) in regard of layout of the writings i like how the date is stamped and i like how the date is pointed out in a dot.
here what to write on tickets
The name of the recital
Issued by Veluzzo
MORVANE
(Find me a sentence that means admit one)
we do need numbers as the seats are numbered
so all in all i would like the invitation and ticket to go together i was thinking of having the dancer bridge xray on invitation and the pointed feet on the ticket.
if you have any other nice parts of the body xray that somehow show its a dancer im also open to that.
than main idea is to have a nice design that is so creative yet simple. play with the fonts to deliver this spooky feeling but all with elegance.
please notice that the picture with the person smoking Xray .. i like how its black and the words are see through with the xray picture. so this would be nice as an idea.
Reason: I still did not find a design that i like.
the theme is asylum. i want it creepy but in the same time ELEGANT. I will be printing invitation on CLEAR paper so the X ray picture could be incorporated in the design in a very subtle way.
Please ask me any question if its not clear
PS my budget is higher now.

```html
<!DOCTYPE html>
<html lang="en">
<head>
<meta charset="utf-8">
<title>MORVANE – Invitation</title>
<link rel="stylesheet" href="https://fonts.googleapis.com/css2?family=Eagle+Lake&family=Questrial&family=Montserrat:wght@600;700&display=swap">
<style>
  :root {
    --page: #ffffff;
    --card: #030303;
    --ink-yellow: #f2d40a;
    --ink-white: #ffffff;
    --grunge: #5c5c5c;
    --bone: #c9c21a;
  }
  * { margin: 0; padding: 0; box-sizing: border-box; }
  html, body {
    width: 1200px; height: 726px; overflow: hidden;
    background: var(--page);
  }
  .invitation-card {
    position: absolute;
    left: 21px; top: 73px;
    width: 724px; height: 362px;
    transform: scale(1.6);
    transform-origin: top left;
    background: var(--card);
    overflow: hidden;
  }
  .edge-texture {
    position: absolute; inset: 0;
    background:
      radial-gradient(ellipse 60px 160px at 100% 40%, rgba(92,92,92,.55), transparent 70%),
      radial-gradient(ellipse 40px 90px at 0% 100%, rgba(92,92,92,.45), transparent 70%),
      radial-gradient(ellipse 80px 30px at 30% 100%, rgba(92,92,92,.25), transparent 70%);
  }
  .xray-figure {
    position: absolute;
    left: 448px; top: 30px;
    width: 265px; height: 270px;
    background: radial-gradient(ellipse 45% 50% at 40% 55%, rgba(201,194,26,.45), rgba(120,120,110,.18) 55%, transparent 80%);
  }
  .recital-title {
    position: absolute;
    left: 44px; top: 42px;
    font-family: "Eagle Lake", serif;
    font-size: 60px;
    letter-spacing: 2px;
    color: var(--ink-yellow);
    line-height: 1;
  }
  .invite-message {
    position: absolute;
    left: 36px; top: 144px;
    width: 420px;
    font-family: "Questrial", sans-serif;
    font-size: 13.5px;
    line-height: 18px;
    color: var(--ink-yellow);
  }
  .invite-message .venue { display: block; }
  .date-block {
    position: absolute;
    left: 37px; top: 257px;
    width: 355px;
    font-family: "Montserrat", sans-serif;
    color: var(--ink-white);
  }
  .month-strip {
    display: flex;
    height: 33px;
    border: 1.5px solid var(--ink-yellow);
  }
  .month-strip .cell {
    flex: 1;
    display: flex; align-items: center; justify-content: center;
    border-right: 1.5px solid var(--ink-yellow);
    font-size: 10px; font-weight: 600;
    position: relative;
  }
  .month-strip .cell:last-child { border-right: none; }
  .month-strip .year { font-size: 10px; font-weight: 700; flex: 1.15; }
  .month-strip .month span {
    writing-mode: vertical-rl;
    transform: rotate(180deg);
    letter-spacing: 1px;
  }
  .month-strip .selected::after {
    content: "";
    position: absolute;
    left: 50%; top: 50%;
    width: 9px; height: 9px;
    margin: -6px 0 0 -4px;
    border-radius: 50%;
    background: var(--ink-white);
  }
  .day-row {
    display: flex; justify-content: space-between;
    margin-top: 10px;
    font-size: 7.2px; font-weight: 700;
  }
  .day-row .marked {
    display: inline-block;
    width: 8px; height: 8px;
    border-radius: 50%;
    background: var(--ink-white);
    color: var(--card);
    text-align: center; line-height: 8px;
    font-size: 5px;
  }
  .event-time {
    margin-top: 6px;
    text-align: center;
    font-size: 10px; font-weight: 600;
    letter-spacing: .2px;
  }
</style>
</head>
<body>
  <section class="invitation-card">
    <div class="edge-texture"></div>
    <div class="xray-figure" role="img" aria-label="X-ray image of a dancing skeleton with glowing yellow bones"></div>

    <h1 class="recital-title">MORVANE</h1>

    <p class="invite-message">
      Our production is ready and we are dying to have you around. So crawl on over for a spooktacular happening at
      <span class="venue">IBN TAMRIQ UNIVERSITY AUDITORIUM</span>
    </p>

    <div class="date-block">
      <div class="month-strip">
        <div class="cell year">20</div>
        <div class="cell month"><span>JAN</span></div>
        <div class="cell month"><span>FEB</span></div>
        <div class="cell month"><span>MAR</span></div>
        <div class="cell month"><span>APR</span></div>
        <div class="cell month selected"><span>MAY</span></div>
        <div class="cell month"><span>JUN</span></div>
        <div class="cell month"><span>AUG</span></div>
        <div class="cell month"><span>SEP</span></div>
        <div class="cell month"><span>OCT</span></div>
        <div class="cell month"><span>NOV</span></div>
        <div class="cell month"><span>DEC</span></div>
        <div class="cell year">14</div>
      </div>
      <div class="day-row">
        <span>1</span><span class="marked">2</span><span class="marked">3</span><span>4</span><span>5</span><span>6</span><span>7</span><span>8</span><span>9</span><span>10</span><span>11</span><span>12</span><span>13</span><span>14</span><span>15</span><span>16</span><span>17</span><span>18</span><span>19</span><span>20</span><span>21</span><span>22</span><span>23</span><span>24</span><span>25</span><span>26</span><span>27</span><span>28</span><span>29</span><span>30</span><span>31</span>
      </div>
      <p class="event-time">The undertaking will begin from 1:30pm to 3:30pm</p>
    </div>
  </section>
</body>
</html>
```